Classic, clean, and fun community pool party door hangers

Looking for a classy, but FUn door hangers for a community outreach pool party.
While we are a faith-based organization, we do NOT want this to look religious.
RGB Color # 4c7991
Template included

Target Market(s)

Families

Font styles to use
Sans Serif

Colors
f37122
959595
dbdbdb

Requirements
Must have
• Date: July 26, 2018 Thursday
• Time: 5:30pm - 7:30pm MDT
• Location: Harrowgate Pool: 2840 9th Ave NW, Loveland, CO 80537
• Free food while it lasts, games, prizes, swimming, and raffle
Should not have
• No Religious symbols

```html
<!DOCTYPE html>
<html lang="en">
<head>
<meta charset="utf-8">
<title>Pool Party Door Hanger</title>
<link rel="stylesheet" href="https://fonts.googleapis.com/css2?family=Bubblegum+Sans&family=Michroma&family=Open+Sans:wght@600;700&family=PT+Sans+Narrow&display=swap">
<style>
  :root {
    --page-bg: #e6e6e6;
    --water-deep: #0f6f93;
    --water-mid: #1a9cc4;
    --water-light: #4cc3de;
    --float-yellow: #f2c12e;
    --accent-yellow: #f4c51c;
    --ray-teal: #39b2c4;
    --white: #ffffff;
    --address-blue: #1f9be0;
    --panel: rgba(16, 58, 78, 0.38);
    --ball-red: #f0633a;
    --mattress-pink: #d9557c;
  }
  * { margin: 0; padding: 0; box-sizing: border-box; }
  html, body { width: 1200px; height: 1200px; overflow: hidden; }
  body { background: var(--page-bg); position: relative; }

  .door-hanger {
    position: absolute;
    left: 369px; top: 47px;
    width: 462px; height: 1105px;
    filter: drop-shadow(0 6px 14px rgba(0,0,0,0.25));
  }
  .hanger-shape { position: absolute; inset: 0; }
  .hanger-content { position: absolute; inset: 0; color: var(--white); }

  .title {
    position: absolute; left: 0; width: 100%;
    text-align: center;
    font-family: "Bubblegum Sans", sans-serif;
    color: var(--white);
    line-height: 1;
    text-shadow: 0 2px 4px rgba(0,0,0,0.25);
  }
  .title-pool { top: 312px; font-size: 92px; letter-spacing: 2px; }
  .title-party { top: 392px; font-size: 92px; letter-spacing: 2px; }

  .date-block {
    position: absolute; left: 50px; top: 494px;
    font-family: "Michroma", sans-serif; line-height: 1;
  }
  .date-day { color: var(--accent-yellow); font-size: 22px; }
  .date-num { font-size: 38px; margin-top: 4px; }
  .date-month, .date-year { font-size: 21px; margin-top: 2px; }

  .time-block {
    position: absolute; left: 288px; top: 552px;
    font-family: "Michroma", sans-serif; line-height: 1;
  }
  .time-label { color: var(--accent-yellow); font-size: 14px; }
  .time-row { font-size: 20px; margin-top: 6px; white-space: nowrap; }
  .time-row small { font-size: 10px; }
  .time-row .zone { font-size: 14px; }

  .venue {
    position: absolute; left: 0; width: 100%; top: 636px;
    text-align: center;
    font-family: "Bubblegum Sans", sans-serif;
    font-size: 46px; line-height: 1;
    text-shadow: 0 2px 4px rgba(0,0,0,0.25);
  }
  .address {
    position: absolute; left: 43px; top: 692px;
    width: 362px; height: 32px;
    background: var(--address-blue);
    font-family: "PT Sans Narrow", sans-serif;
    font-size: 23px; line-height: 32px;
    text-align: center; white-space: nowrap;
  }

  .perks-panel {
    position: absolute; left: 23px; top: 740px;
    width: 412px; height: 292px;
    background: var(--panel);
  }
  .perk {
    position: absolute; left: 0; width: 100%;
    text-align: center;
    font-family: "Open Sans", sans-serif; font-weight: 600;
    font-size: 27px; line-height: 1; white-space: nowrap;
  }
  .perk-1 { top: 20px; }
  .perk-2 { top: 77px; }
  .perk-3 { top: 134px; }
  .perk-4 { top: 192px; }
  .waves { position: absolute; inset: 0; }

  .beach-ball {
    position: absolute; left: 31px; top: 985px;
    width: 84px; height: 84px; border-radius: 50%;
    background: var(--ball-red);
  }
  .air-mattress {
    position: absolute; left: 353px; top: 945px;
    width: 72px; height: 132px;
    background: var(--mattress-pink);
    border-radius: 6px;
    transform: rotate(25deg);
  }
</style>
</head>
<body>
  <div class="door-hanger">
    <svg class="hanger-shape" width="462" height="1105" viewBox="0 0 462 1105">
      <defs>
        <mask id="hanger-cutout">
          <rect x="0" y="0" width="462" height="1105" fill="#fff"/>
          <circle cx="230" cy="170" r="95" fill="#000"/>
          <polygon points="118,0 150,0 212,92 186,108" fill="#000"/>
        </mask>
        <radialGradient id="pool-photo" cx="0.5" cy="0.45" r="0.7">
          <stop offset="0" stop-color="var(--float-yellow)"/>
          <stop offset="0.22" stop-color="var(--water-light)"/>
          <stop offset="0.6" stop-color="var(--water-mid)"/>
          <stop offset="1" stop-color="var(--water-deep)"/>
        </radialGradient>
      </defs>
      <g mask="url(#hanger-cutout)">
        <rect x="0" y="0" width="462" height="1105" fill="url(#pool-photo)" role="img" aria-label="Aerial photo of a person relaxing on a yellow swim ring in sparkling blue pool water"/>
        <rect x="7" y="7" width="448" height="1091" fill="none" stroke="var(--white)" stroke-width="1"/>
      </g>
      <g class="sun-rays" stroke="var(--ray-teal)" stroke-width="7" stroke-linecap="round">
        <line x1="115" y1="228" x2="140" y2="270"/>
        <line x1="30" y1="332" x2="78" y2="358"/>
        <line x1="40" y1="475" x2="75" y2="450"/>
        <line x1="335" y1="270" x2="375" y2="240"/>
        <line x1="368" y1="360" x2="410" y2="332"/>
        <line x1="385" y1="465" x2="425" y2="505"/>
      </g>
    </svg>

    <div class="hanger-content">
      <div class="title title-pool">POOL</div>
      <div class="title title-party">PARTY</div>

      <div class="date-block">
        <div class="date-day">THU</div>
        <div class="date-num">26</div>
        <div class="date-month">JULY</div>
        <div class="date-year">2018</div>
      </div>

      <div class="time-block">
        <div class="time-label">TIME</div>
        <div class="time-row">5:30<small>PM</small></div>
        <div class="time-row">7:30<small>PM</small> <span class="zone">MDT</span></div>
      </div>

      <div class="venue">HARROWGATE POOL</div>
      <div class="address">2840 9th Ave NW, Loveland, CO 80537</div>

      <div class="perks-panel">
        <svg class="waves" width="412" height="292" viewBox="0 0 412 292" fill="none" stroke="var(--accent-yellow)" stroke-width="3" stroke-linecap="round">
          <path d="M25 64 q22 -8 44 0 t44 0 t44 0 t44 0 t44 0 t44 0 t44 0 t44 0"/>
          <path d="M75 122 q20 -7 40 0 t40 0 t40 0 t40 0 t40 0 t40 0 t40 0"/>
          <path d="M75 180 q20 -7 40 0 t40 0 t40 0 t40 0 t40 0 t40 0 t40 0"/>
          <path d="M142 244 q16 -7 32 0 t32 0 t32 0 t32 0"/>
        </svg>
        <div class="perk perk-1">Free food, games, prizes,</div>
        <div class="perk perk-2">swimming, and raffle</div>
        <div class="perk perk-3">Free food while it last!</div>
        <div class="perk perk-4">Free admission</div>
      </div>

      <div class="beach-ball" role="img" aria-label="Illustration of a striped beach ball"></div>
      <div class="air-mattress" role="img" aria-label="Illustration of a pink inflatable pool mattress"></div>
    </div>
  </div>
</body>
</html>
```